Stationary and business card for an electrical contractor
Norvik Electric LLC
Stationary and business card for an electrical contractor - Construction
Creative Brief
Simple
Glen Hadley
President
412 N Orchard Ave
glen@norvikelectric-example.biz
WA Cont. # NORVIEL352TQ

```html
<!DOCTYPE html>
<html lang="en">
<head>
<meta charset="utf-8">
<title>Norvik Electric LLC – Business Card</title>
<link href="https://fonts.googleapis.com/css2?family=Montserrat:wght@400;600;800&display=swap" rel="stylesheet">
<style>
  :root {
    --backdrop: #8a8a8a;
    --card-black: #0b0b0b;
    --card-black-sheen: #262626;
    --card-white: #ffffff;
    --brand-red: #e0203a;
    --text-light: #ffffff;
    --text-dark: #111111;
  }
  * { margin: 0; padding: 0; box-sizing: border-box; }
  html, body {
    width: 1200px; height: 908px; overflow: hidden;
    background: var(--backdrop);
    font-family: "Montserrat", Arial, sans-serif;
  }
  .sheet {
    width: 1200px; height: 908px;
    display: flex; flex-direction: column;
    align-items: center; justify-content: center; gap: 40px;
  }
  .card {
    position: relative;
    width: 700px; height: 400px;
    border-radius: 22px;
    overflow: hidden;
  }
  /* Front */
  .card--front {
    background: linear-gradient(135deg, var(--card-black-sheen) 0%, var(--card-black) 45%, var(--card-black) 100%);
    display: flex; align-items: center; justify-content: center;
  }
  .wordmark {
    display: flex; align-items: center; gap: 14px;
    font-weight: 800; font-size: 40px; letter-spacing: 1px;
    text-transform: uppercase;
  }
  .wordmark__dot {
    width: 22px; height: 22px; border-radius: 50%;
    background: var(--brand-red);
  }
  .card--front .wordmark { color: var(--text-light); }
  /* Back */
  .card--back { background: var(--card-white); }
  .back-shape { position: absolute; inset: 0; }
  .card--back .wordmark {
    position: absolute; left: 48px; top: 50%;
    transform: translateY(-50%);
    font-size: 32px; color: var(--text-dark);
  }
  .contact {
    position: absolute; right: 40px; top: 52px;
    text-align: right; color: var(--text-light);
  }
  .contact__name { font-size: 26px; font-weight: 400; }
  .contact__title { font-size: 16px; color: var(--brand-red); margin-top: 2px; }
  .contact__list { list-style: none; margin-top: 56px; font-size: 13px; line-height: 1.9; }
  .contact__license { color: var(--brand-red); font-size: 11px; }
  .contact__item { display: flex; align-items: center; justify-content: flex-end; gap: 8px; }
  .icon { width: 16px; height: 16px; flex: none; }
</style>
</head>
<body>
<main class="sheet">
  <section class="card card--front" aria-label="Business card front">
    <div class="wordmark"><span class="wordmark__dot"></span><span>Norvik Electric</span></div>
  </section>

  <section class="card card--back" aria-label="Business card back">
    <svg class="back-shape" viewBox="0 0 700 400" width="700" height="400" aria-hidden="true">
      <path d="M470 0 Q330 200 470 400 L700 400 L700 0 Z" fill="var(--card-black)"/>
      <path d="M455 0 Q315 200 455 400" fill="none" stroke="var(--brand-red)" stroke-width="14"/>
    </svg>
    <div class="wordmark"><span>Norvik Electric</span></div>
    <div class="contact">
      <p class="contact__name">Glen Hadley</p>
      <p class="contact__title">President</p>
      <ul class="contact__list">
        <li class="contact__license">WA Cont. # NORVIEL352TQ</li>
        <li class="contact__item">412 N Orchard Ave</li>
        <li class="contact__item">360 555 0148
          <svg class="icon" viewBox="0 0 16 16" aria-hidden="true"><circle cx="8" cy="8" r="7.5" fill="var(--brand-red)"/><path d="M5.5 4.5 L7 4.5 L7.6 6.3 L6.8 7 Q7.6 8.6 9 9.2 L9.7 8.4 L11.5 9 L11.5 10.5 Q7 11 5 6 Z" fill="#fff"/></svg>
        </li>
        <li class="contact__item">glen@norvikelectric-example.biz
          <svg class="icon" viewBox="0 0 16 16" aria-hidden="true"><circle cx="8" cy="8" r="7.5" fill="var(--brand-red)"/><rect x="4" y="5.5" width="8" height="5.5" fill="#fff"/><path d="M4 5.5 L8 8.6 L12 5.5" fill="none" stroke="var(--brand-red)" stroke-width="0.9"/></svg>
        </li>
      </ul>
    </div>
  </section>
</main>
</body>
</html>
```